Stylish but eye catching vehicle signage for a Building and Carpentry business based in Sydney.**

We need vehicle signage for our White 2013 KR Halvane Van. We are not looking for a full wrap just signage that is eye catching, and memorable. Although we are a construction business our branding and Logo is sophisticated and clean and had a modern design . We would like to have vehicle branding that is consistent with that .

Our Logo is in grey and we would like to keep the design eye catching without using bright colours, we are not opposed to colour , we have used greys and ocre (brownish yellow)is our branding and would consider designs using these colours.

We would like to see designs that are stylish and sophisticated and not ones featuring tools or equipment for construction . We would like to see designs that portray our skills in the field of design .

Below I will attach our full logo and some examples of vehicle signage we like.
We would like the logo and contact details (email address and mobile number) on the sides and back.
We would also like the description
' new builds I renovations I residential I commercial '
at the bottom of the sides of the car between the wheels.
Updates

Hi Designers The contact details we would like on the vehicle are: 0491 358 064 rdeacyconstruction@postvane.net Just those two. Thanks

Target Market(s)

We would like to attract clients that are looking for quality work done right and professionally , and are happy to pay for good quality.

Contact Information for Business Card

I would like to go for a business card design that will accomodate embossing .
I would like the full logo on the front of the business card , no contact infomation.
The house or building icon in our logo will be raised or embossed by the printing company, so the back or the card will show the icon debossed (indented) .
On the back of the business card I would like the contact person's details:
ROWAN DEACY
carpenter
project manager
....and also the email address and mobile number on the back too.

Font styles to use
Sans Serif
Other font styles liked:
• Futura Lt Bt

Colors

Designer to choose only greyscale colors for use in the design.

Requirements
Must have
• Our logo (big and clear) and mobile number and email address on both sides and the back
Nice to have
• Designs or patterns that look architectural and elegant.
Should not have
• Any construction tools or equipment .
Designs like flames or lightning bolts
Too much colour or very bright colours

```html
<!DOCTYPE html>
<html lang="en">
<head>
<meta charset="utf-8">
<title>R Deacy Construction — Business Card</title>
<link href="https://fonts.googleapis.com/css2?family=Jost:wght@300;400&display=swap" rel="stylesheet">
<style>
  :root {
    --page-bg: #ffffff;
    --card-grey: #6b6b6b;
    --ink-light: #ffffff;
  }
  * { margin: 0; padding: 0; box-sizing: border-box; }
  html, body {
    width: 1200px;
    height: 1200px;
    overflow: hidden;
    background: var(--page-bg);
    font-family: 'Jost', 'Futura', sans-serif;
    color: var(--ink-light);
  }
  .canvas { position: relative; width: 1200px; height: 1200px; }

  .card {
    position: absolute;
    left: 319px;
    width: 562px;
    height: 325px;
    background: var(--card-grey);
    overflow: hidden;
  }
  .card--front { top: 194px; }
  .card--back { top: 691px; }

  /* Front: company name lockup */
  .brand {
    position: absolute;
    left: 128px;
    top: 112px;
    font-weight: 300;
    line-height: 1;
  }
  .brand__name {
    display: block;
    font-size: 74px;
    letter-spacing: 3px;
  }
  .brand__sub {
    display: block;
    margin-top: 10px;
    font-size: 31px;
    letter-spacing: 1.5px;
  }
  .brand__tagline {
    position: absolute;
    left: 128px;
    top: 232px;
    font-size: 19px;
    font-weight: 300;
    letter-spacing: 1.2px;
  }

  /* Back: contact person */
  .person {
    position: absolute;
    left: 146px;
    top: 176px;
    font-weight: 300;
  }
  .person__name {
    font-size: 23px;
    letter-spacing: 0.5px;
    line-height: 1;
  }
  .person__rule {
    width: 36px;
    height: 2px;
    background: var(--ink-light);
    margin: 10px 0 8px;
  }
  .person__role {
    font-size: 22px;
    letter-spacing: 2px;
    line-height: 1.2;
  }

  /* Back: vertical contact lines, reading bottom to top */
  .contact__line {
    position: absolute;
    top: 301px;
    white-space: nowrap;
    font-weight: 300;
    line-height: 1;
    transform-origin: 0 0;
    transform: rotate(-90deg);
  }
  .contact__phone {
    left: 456px;
    font-size: 23px;
    letter-spacing: 1.5px;
  }
  .contact__email {
    left: 489px;
    font-size: 16.5px;
  }
</style>
</head>
<body>
  <main class="canvas">
    <section class="card card--front" aria-label="Business card front">
      <h1 class="brand">
        <span class="brand__name">R DEACY</span>
        <span class="brand__sub">CONSTRUCTION</span>
      </h1>
      <p class="brand__tagline">BUILDING AND CARPENTRY</p>
    </section>

    <section class="card card--back" aria-label="Business card back">
      <div class="person">
        <p class="person__name">ROWAN DEACY</p>
        <div class="person__rule"></div>
        <p class="person__role">project manager<br>carpenter</p>
      </div>
      <p class="contact__line contact__phone">0491 358 064</p>
      <p class="contact__line contact__email">rdeacyconstruction@postvane.net</p>
    </section>
  </main>
</body>
</html>
```